Beauty Salon
I would like to see designs using sky blue and a soft orange. Mainly I would like my name ( Glow N' Wave Salon ) used as the design

Industry/Entity Type

Business

Contact Information for Business Card

Sky Ripple Salon
418 E Maple Dr #14
Brookvale, Ca 90210
909 555-0172

```html
<!DOCTYPE html>
<html lang="en">
<head>
<meta charset="utf-8">
<title>Sky Ripple Salon — Business Card</title>
<link rel="stylesheet" href="https://fonts.googleapis.com/css2?family=Playball&family=Open+Sans:wght@400&display=swap">
<style>
  :root {
    --soft-orange: #f27a21;
    --sky-blue: #3db6e8;
    --card-white: #ffffff;
    --backdrop: #ece8e2;
    --card-shadow: rgba(60, 40, 20, 0.22);
  }
  * { margin: 0; padding: 0; box-sizing: border-box; }
  html, body {
    width: 1200px;
    height: 900px;
    overflow: hidden;
    background: var(--backdrop);
  }
  .canvas {
    position: relative;
    width: 1200px;
    height: 900px;
  }
  .card {
    position: absolute;
    left: 300px;
    width: 600px;
    height: 343px;
    background: var(--soft-orange);
    box-shadow: 0 10px 28px var(--card-shadow);
    overflow: hidden;
  }
  .card--front { top: 86px; }
  .card--back { top: 471px; }
  .card__art {
    position: absolute;
    inset: 0;
    width: 100%;
    height: 100%;
  }
  .card__wave { fill: var(--sky-blue); }
  .salon-name {
    position: absolute;
    font-family: "Playball", cursive;
    font-weight: 400;
    color: var(--card-white);
    white-space: nowrap;
    line-height: 1;
  }
  .card--front .salon-name {
    top: 30px;
    left: 40px;
    font-size: 38px;
  }
  .card--back .salon-name {
    top: 150px;
    right: 40px;
    font-size: 40px;
  }
  .contact {
    position: absolute;
    left: 40px;
    bottom: 34px;
    font-family: "Open Sans", sans-serif;
    font-size: 15px;
    line-height: 1.45;
    color: var(--card-white);
    font-style: normal;
  }
</style>
</head>
<body>
<main class="canvas">
  <section class="card card--front" aria-label="Business card front">
    <svg class="card__art" viewBox="0 0 600 343" role="img" aria-label="Flowing sky blue hair ornament sweeping across the card">
      <path class="card__wave" d="M0 235 C 70 205, 120 225, 190 200 C 260 175, 300 150, 360 120 C 420 90, 470 100, 520 70 C 560 45, 585 35, 600 30 L 600 343 L 0 343 Z"/>
    </svg>
    <h1 class="salon-name">Sky Ripple Salon</h1>
    <address class="contact">
      418 E Maple Dr #14<br>
      Brookvale, Ca 90210<br>
      909 555-0172
    </address>
  </section>

  <section class="card card--back" aria-label="Business card back">
    <svg class="card__art" viewBox="0 0 600 343" role="img" aria-label="Flowing sky blue hair ornament along the left side">
      <path class="card__wave" d="M0 0 L 210 0 C 200 40, 235 70, 215 110 C 195 150, 245 180, 225 225 C 205 270, 250 300, 235 343 L 0 343 Z"/>
    </svg>
    <h2 class="salon-name">Sky Ripple Salon</h2>
  </section>
</main>
</body>
</html>
```